Kestrel Dental personal information forms

We are a Dental Practice that require an update to our information forms, there are 3 versions of it.
I will attach our old ones, we need to keep the same information on there, we just want them to look better and use our current logo and colours.
Our website is www.kestreldental.net
Our facebook is www.friendnook.com/kestreldentalbrookplaza/
..................................................................................................

Target Market(s)

Everyone, easy to read

Industry/Entity Type

Dental Clinic

Colors
0692cd
34a6d7
cee9f5
ffffff
0255a3
3276b5

Requirements
Must have
• Logo
• Our colours
• same information as the uploaded versions
Should not have
• any other colour besides the blues, black and white

```html
<!DOCTYPE html>
<html lang="en">
<head>
<meta charset="utf-8">
<title>Kestrel Dental – Medical History Update</title>
<link href="https://fonts.googleapis.com/css2?family=Nunito+Sans:wght@400;600;700;800&display=swap" rel="stylesheet">
<style>
  :root {
    --blue-deep: #0255a3;
    --blue-main: #0692cd;
    --blue-mid: #3276b5;
    --blue-soft: #34a6d7;
    --blue-pale: #cee9f5;
    --white: #ffffff;
    --ink: #111111;
    --rule: #d4d4d4;
    --row-fill: #e4e4e4;
    --crop: #222222;
  }
  * { box-sizing: border-box; margin: 0; padding: 0; }
  html, body { width: 880px; height: 1200px; overflow: hidden; background: var(--white); }
  body { position: relative; font-family: "Nunito Sans", Arial, sans-serif; color: var(--ink); }

  .crop { position: absolute; background: var(--crop); }
  .crop--v { width: 1px; height: 34px; }
  .crop--h { height: 1px; width: 42px; }

  .sheet { position: absolute; left: 43px; top: 43px; width: 794px; height: 1113px; background: var(--white); }

  .masthead {
    position: absolute; left: 0; top: 0; width: 100%; height: 109px;
    background: radial-gradient(ellipse 60% 120% at 55% 60%, var(--blue-soft) 0%, var(--blue-main) 45%, #0a6fe0 100%);
  }
  .masthead__stripe {
    position: absolute; left: 0; top: 112px; width: 100%; height: 11px;
    background: linear-gradient(90deg, var(--blue-main), var(--blue-soft) 50%, var(--blue-main));
  }
  .brand {
    position: absolute; left: 0; top: 0; width: 100%; height: 109px;
    display: flex; align-items: center; justify-content: center; gap: 12px;
    color: var(--white); font-weight: 700; font-size: 34px; line-height: 1;
  }
  .brand__dot { width: 16px; height: 16px; border-radius: 50%; background: var(--white); }

  .footband {
    position: absolute; left: 0; bottom: 0; width: 100%; height: 43px;
    background: radial-gradient(ellipse 40% 140% at 50% 100%, var(--blue-soft) 0%, var(--blue-main) 50%, #0a6fe0 100%);
  }

  .practitioner { position: absolute; left: 33px; top: 174px; color: var(--blue-main); font-weight: 800; font-size: 14.5px; line-height: 19px; }
  .sticker-box {
    position: absolute; left: 478px; top: 163px; width: 281px; height: 59px;
    border: 1px solid var(--rule); display: flex; align-items: center; justify-content: center;
    font-style: italic; font-size: 12.5px;
  }

  .intro { position: absolute; left: 33px; top: 270px; width: 725px; }
  .intro__welcome { color: var(--blue-main); font-size: 15.5px; margin-bottom: 7px; }
  .intro__text { font-size: 15px; line-height: 19.5px; text-align: justify; letter-spacing: 0.1px; }
  .intro__text strong { font-weight: 800; }

  .history { position: absolute; left: 33px; top: 397px; width: 728px; border: 1px solid var(--rule); border-top: none; }
  .history__question { position: relative; padding: 5px 70px 0 8px; font-size: 12px; line-height: 15px; border-top: 1px solid var(--rule); }
  .history__question--tall { height: 43px; }
  .history__question--mid { height: 36px; }
  .history__question--short { height: 21px; padding-top: 3px; }
  .history__answer { position: absolute; right: 8px; top: 5px; font-weight: 800; font-size: 11.5px; }
  .history__question--short .history__answer { top: 4px; }
  .history__fill { height: 22px; background: var(--row-fill); }
  .history__end { height: 13px; border-top: 1px solid var(--rule); }

  .conditions { height: 208px; border-top: 1px solid var(--rule); padding: 9px 8px 0; font-size: 12px; }
  .conditions__grid { display: grid; grid-template-columns: 233px 238px 200px; margin-top: 9px; padding-left: 16px; }
  .conditions__list { list-style: none; }
  .conditions__list li { font-size: 11.5px; line-height: 17.3px; display: flex; align-items: center; }
  .tickbox { display: inline-block; width: 8px; height: 8px; border: 1.3px solid var(--ink); margin-right: 10px; box-shadow: 1px 1px 0 var(--ink); }

  .declaration { position: absolute; left: 33px; top: 953px; width: 715px; font-weight: 800; font-size: 11.3px; line-height: 15px; }
  .signoff { position: absolute; left: 33px; top: 995px; width: 740px; font-size: 11px; display: flex; }
  .signoff__role { width: 317px; }
  .signoff__field { display: flex; align-items: flex-end; }
  .signoff__field--sign { width: 211px; }
  .signoff__line { display: inline-block; border-bottom: 1px solid #777; margin-left: 6px; height: 11px; width: 129px; }
</style>
</head>
<body>
  <span class="crop crop--v" style="left:54px;top:0"></span>
  <span class="crop crop--v" style="left:825px;top:0"></span>
  <span class="crop crop--v" style="left:54px;top:1166px"></span>
  <span class="crop crop--v" style="left:825px;top:1166px"></span>
  <span class="crop crop--h" style="left:0;top:58px"></span>
  <span class="crop crop--h" style="left:838px;top:58px"></span>
  <span class="crop crop--h" style="left:0;top:1142px"></span>
  <span class="crop crop--h" style="left:838px;top:1142px"></span>

  <main class="sheet">
    <header class="masthead">
      <div class="brand"><span class="brand__dot"></span><span class="brand__name">Kestrel Dental</span></div>
    </header>
    <div class="masthead__stripe"></div>

    <div class="practitioner">Dr. Peter Halloran<br>Dental Surgeon</div>
    <div class="sticker-box">Affix patient sticker here.</div>

    <section class="intro">
      <p class="intro__welcome">Welcome back to our practice!</p>
      <p class="intro__text"><strong>THIS INFORMATION IS CONFIDENTIAL</strong> and is necessary to enable us to offer you <strong>THE BEST POSSIBLE CARE</strong>. It is now mandatory to have a written updated medical history every two years and we would appreciate your time in thoroughly completing this form.</p>
    </section>

    <section class="history">
      <div class="history__question history__question--tall">&nbsp;Are you currently or have you taken any medication or dietary supplements in the last 12 months?<br>(If YES, please list below)<span class="history__answer">YES/NO</span></div>
      <div class="history__fill"></div>
      <div class="history__question history__question--mid">Allergies/Reactions?<br>(If YES, please list below)<span class="history__answer">YES/NO</span></div>
      <div class="history__fill"></div>

      <div class="conditions">
        <p>Have you ever had or are you suffering from any of the following? Please tick any that apply:</p>
        <div class="conditions__grid">
          <ul class="conditions__list">
            <li><span class="tickbox"></span>Rheumatic fever</li>
            <li><span class="tickbox"></span>Epilepsy</li>
            <li><span class="tickbox"></span>Asthma</li>
            <li><span class="tickbox"></span>Tuberculosis</li>
            <li><span class="tickbox"></span>Radiation therapy</li>
            <li><span class="tickbox"></span>Dizziness, fainting</li>
            <li><span class="tickbox"></span>Hepatitis A B or C</li>
            <li><span class="tickbox"></span>Recent eye surgery</li>
          </ul>
          <ul class="conditions__list">
            <li><span class="tickbox"></span>Diabetes</li>
            <li><span class="tickbox"></span>Kidney disease</li>
            <li><span class="tickbox"></span>Heart attack</li>
            <li><span class="tickbox"></span>High blood pressure</li>
            <li><span class="tickbox"></span>Bleeding problems</li>
            <li><span class="tickbox"></span>Artificial joints</li>
            <li><span class="tickbox"></span>Respiratory problems</li>
          </ul>
          <ul class="conditions__list">
            <li><span class="tickbox"></span>HIV positive</li>
            <li><span class="tickbox"></span>High cholesterol</li>
            <li><span class="tickbox"></span>Cancer</li>
            <li><span class="tickbox"></span>Pace-maker</li>
            <li><span class="tickbox"></span>Osteoporosis</li>
            <li><span class="tickbox"></span>Heart rate problems</li>
            <li><span class="tickbox"></span>Heart murmur</li>
          </ul>
        </div>
      </div>

      <div class="history__question history__question--short">Do you have any disease, condition or problem not listed above? (If YES, please give details)<span class="history__answer">YES/NO</span></div>
      <div class="history__fill"></div>
      <div class="history__question history__question--short">Have you had surgery or been to hospital in the last 5 years? (If YES, please give details)<span class="history__answer">YES/NO</span></div>
      <div class="history__fill"></div>
      <div class="history__question history__question--short">&nbsp;For women: Are you pregnant? (If YES, how many months?)<span class="history__answer">YES/NO</span></div>
      <div class="history__fill"></div>
      <div class="history__question history__question--short">Do you currently or have you ever smoked?<span class="history__answer">YES/NO</span></div>
      <div class="history__fill"></div>
      <div class="history__end"></div>
    </section>

    <p class="declaration">The information that I have provided is to the best of my knowledge true and I understand that it is my responsibility to inform the practice of any changes in my medical status.</p>
    <div class="signoff">
      <span class="signoff__role">Patient/Parent/Person Responsible</span>
      <span class="signoff__field signoff__field--sign">Signature:<span class="signoff__line"></span></span>
      <span class="signoff__field">Date:<span class="signoff__line"></span></span>
    </div>

    <footer class="footband"></footer>
  </main>
</body>
</html>
```